Business Card for Jewelry Business

We need a new namecard design for a jewelry company based in Bangkok, Thailand. We have a new website recently and want the new namecard to reflect our new modern image. I have uploaded our old namecard to show you the information that needs to be on the namecard. Pls check our website www.qelburn.com for the new color scheme to help design the new namecard.

```html
<!DOCTYPE html>
<html lang="en">
<head>
<meta charset="utf-8">
<title>Qelburn Manufacturers – Business Card</title>
<link rel="stylesheet" href="https://fonts.googleapis.com/css2?family=Jost:wght@300;400&display=swap">
<style>
  :root {
    --paper: #ffffff;
    --ink: #1b1b1f;
    --mint: #63ffc8;
    --stone: #dcdbcf;
    --frame: #222222;
  }
  html, body {
    margin: 0;
    padding: 0;
    width: 1200px;
    height: 686px;
    overflow: hidden;
    background: var(--paper);
  }
  .card {
    position: relative;
    width: 1200px;
    height: 686px;
    box-sizing: border-box;
    border: 1px solid var(--frame);
    background: var(--paper);
    overflow: hidden;
    font-family: "Jost", "Helvetica Neue", Arial, sans-serif;
    color: var(--ink);
  }
  .card__waves {
    position: absolute;
    inset: 0;
    width: 100%;
    height: 100%;
  }
  .wave--mint { fill: var(--mint); }
  .wave--stone { fill: var(--stone); }
  .wave--paper { fill: var(--paper); }

  .brand {
    position: absolute;
    left: 0;
    right: 0;
    top: 248px;
    display: flex;
    align-items: center;
    justify-content: center;
    gap: 22px;
  }
  .brand__dot {
    width: 34px;
    height: 34px;
    border-radius: 50%;
    background: var(--mint);
    flex: none;
  }
  .brand__name {
    margin: 0;
    font-size: 40px;
    font-weight: 400;
    letter-spacing: 0.12em;
    line-height: 1;
    color: var(--ink);
  }
  .tagline {
    position: absolute;
    left: 0;
    right: 0;
    top: 463px;
    margin: 0;
    text-align: center;
    font-size: 35px;
    font-weight: 300;
    letter-spacing: 0.12em;
    line-height: 1;
    color: var(--ink);
  }
</style>
</head>
<body>
  <div class="card">
    <svg class="card__waves" viewBox="0 0 1200 686" preserveAspectRatio="none" aria-hidden="true">
      <rect class="wave--mint" x="0" y="0" width="1200" height="686"/>
      <path class="wave--stone" d="M0 0 H1200 V511 Q600 723 0 511 Z"/>
      <path class="wave--paper" d="M0 0 H1200 V469 Q600 709 0 469 Z"/>
    </svg>

    <div class="brand">
      <span class="brand__dot"></span>
      <h1 class="brand__name">QELBURN MANUFACTURERS</h1>
    </div>

    <p class="tagline">FINE GOLD AND SILVER JEWELRY</p>
  </div>
</body>
</html>
```